Multi Page Booklet/Brochure- Cataloogue requested for Trevik

We have an industrial packaging company that has a product listing that needs to have a product feature catalog. It could also be a multiple page brochure with features and benefits of the product. Our main core products are:
Gaylord Boxes
FIBC Bulk Bags
Stretch Film
Packaging Tape
Liners

We would like to have a 2-3 page layout of each section that shows the features and benefits.

We are in the middle of a web site redesign, but you can look at our current web site that will show our products and business.

We will want photos, but don't have a lot and may need to have that done to add to the brochure.

                                        To get more information on the company, please look at trevikco.example

This site is our old site but will give you a good reference of our products.  The new site in still on a test site and under construction.

Target Market(s)

Manufactures of any product, recycling companies (Plastic, metal, textile etc..), food processors, mining companies, oil companies

Industry/Entity Type

Industrial

Requirements
Must have
• Must be able to be bound like a book or magazine.
• Must have Feature pages of each product with Features and Benefits, then the line of product with images.

```html
<!DOCTYPE html>
<html lang="en">
<head>
<meta charset="utf-8">
<title>Trevik Product Brochure</title>
<link rel="stylesheet" href="https://fonts.googleapis.com/css2?family=Open+Sans:ital,wght@0,400;0,600;0,700;0,800;1,700&display=swap">
<style>
:root{
  --bg:#2b2b2d;
  --blue:#1f4fa3;
  --blue-dark:#143a7e;
  --blue-light:#4d8fd6;
  --lime:#d8e83a;
  --white:#ffffff;
  --paper:#f7f9fc;
  --ink:#3a4250;
  --muted:#8a94a4;
  --caption:#e6e6e6;
}
*{box-sizing:border-box;margin:0;padding:0}
html,body{width:849px;height:1200px;overflow:hidden}
body{background:var(--bg);font-family:"Open Sans",Arial,sans-serif;position:relative;color:var(--ink)}
.piece{position:absolute}
.caption{position:absolute;color:var(--caption);font-size:19px;font-weight:400;text-align:center;width:100%;left:0}
.page{position:absolute;overflow:hidden;background:var(--white)}
.spread{display:flex;position:absolute;box-shadow:0 6px 18px rgba(0,0,0,.45)}
.spread .page{position:relative}

/* Cover */
.cover{background:linear-gradient(180deg,var(--blue-light),var(--blue) 55%,var(--blue-dark))}
.cover .top{position:absolute;left:0;top:0;width:100%;height:15%;background:var(--white)}
.brand{font-weight:800;color:var(--blue);letter-spacing:.04em;display:flex;align-items:center;gap:5px}
.brand .mark{background:var(--blue);display:inline-block}
.cover .brand{position:absolute;left:12%;top:5%}
.cover .bands{position:absolute;inset:0}
.cover .photo{position:absolute;right:6%;bottom:12%;width:48%;height:26%;background:linear-gradient(160deg,#d9c6a0,#b4966a 60%,#e9e9ea);border-radius:2px}
.cover .slogan{position:absolute;left:9%;top:44%;color:var(--white);font-weight:700;line-height:1.15}
.cover .slogan em{font-style:normal;color:var(--lime)}
.cover .slogan .tag{display:block;font-weight:600;font-style:italic;color:var(--white);margin-top:6px}

/* Back cover */
.back{background:linear-gradient(180deg,var(--blue-light),var(--blue) 60%,var(--blue-dark))}
.back .band{position:absolute;left:0;top:58%;width:100%;height:26%;background:var(--white)}
.back .brand{position:absolute;left:12%;top:62%;font-size:12px}
.back .contact{position:absolute;left:12%;top:70%;font-size:6px;line-height:1.5;color:var(--ink)}

/* Inside pages */
.inside{background:var(--paper)}
.inside .tab{position:absolute;top:8%;height:7%;background:var(--blue);color:var(--white);font-size:7px;font-weight:700;display:flex;align-items:center;padding:0 8px;letter-spacing:.05em}
.inside .tab.left{left:0;width:38%}
.inside .tab.right{right:0;width:45%;justify-content:flex-end}
.inside .title{position:absolute;color:var(--blue);font-weight:700;font-size:10px}
.inside .body{position:absolute;font-size:5.5px;line-height:1.6;color:var(--ink)}
.inside .img{position:absolute;border-radius:2px}
.inside .foot{position:absolute;left:0;bottom:0;width:100%;height:4%;background:var(--blue)}
.swatches{position:absolute;display:grid;grid-template-columns:repeat(6,1fr);gap:3px}
.swatches span{height:10px;border-radius:1px}
.spec{position:absolute;border-collapse:collapse;font-size:5.5px;color:var(--ink)}
.spec th{background:var(--blue);color:var(--white);font-weight:700;padding:2px 5px}
.spec td{padding:2px 5px;border-bottom:1px solid #cfd6e2}
.spine{width:1px;background:rgba(0,0,0,.15)}
</style>
</head>
<body>

<!-- Back cover and cover spread -->
<section class="piece" style="left:30px;top:70px;width:400px;height:330px">
  <div class="spread" style="left:10px;top:0">
    <div class="page back" style="width:190px;height:268px">
      <div class="band"></div>
      <div class="brand"><span class="mark" style="width:8px;height:8px"></span>TREVIK</div>
      <div class="contact">Industrial Packaging Supply<br>1200 Harbor Road, Dayton OH<br>Tel (555) 014-2290<br>trevikco.example</div>
    </div>
    <div class="spine"></div>
    <div class="page cover" style="width:190px;height:268px">
      <svg class="bands" viewBox="0 0 190 268" preserveAspectRatio="none"><polygon points="120,40 190,40 190,150 150,268 80,268" fill="var(--lime)" opacity=".9"/><polygon points="150,40 190,40 190,110" fill="var(--white)" opacity=".35"/></svg>
      <div class="top"></div>
      <div class="brand" style="font-size:11px"><span class="mark" style="width:7px;height:7px"></span>TREVIK</div>
      <div class="slogan" style="font-size:9px"><em>Quality</em> Products<br>and Services<span class="tag" style="font-size:7px">not the Quantity</span></div>
      <div class="photo" role="img" aria-label="Photo of stacked cardboard boxes and bulk bags"></div>
    </div>
  </div>
  <p class="caption" style="top:282px">Back Cover &amp; Cover</p>
</section>

<!-- Cover -->
<section class="piece" style="left:480px;top:40px;width:330px;height:460px">
  <div class="page cover" style="left:40px;top:0;width:250px;height:354px;box-shadow:0 6px 18px rgba(0,0,0,.45)">
    <svg class="bands" viewBox="0 0 250 354" preserveAspectRatio="none"><polygon points="160,53 250,53 250,200 200,354 105,354" fill="var(--lime)" opacity=".9"/><polygon points="200,53 250,53 250,145" fill="var(--white)" opacity=".35"/></svg>
    <div class="top"></div>
    <div class="brand" style="font-size:15px"><span class="mark" style="width:10px;height:10px"></span>TREVIK</div>
    <div class="slogan" style="font-size:13px"><em>Quality</em> Products<br>and Services<span class="tag" style="font-size:10px">not the Quantity</span></div>
    <div class="photo" role="img" aria-label="Photo of stacked cardboard boxes and bulk bags"></div>
  </div>
  <p class="caption" style="top:385px">Cover</p>
</section>

<!-- Inside pages 2 & 3 -->
<section class="piece" style="left:30px;top:610px;width:390px;height:340px">
  <div class="spread" style="left:10px;top:0">
    <div class="page inside" style="width:185px;height:262px">
      <div class="tab left">PRODUCTS</div>
      <div class="title" style="left:12%;top:22%">Gaylord Boxes</div>
      <div class="body" style="left:12%;top:29%;width:76%">Heavy duty corrugated boxes for bulk storage<br>Available in many sizes and wall grades</div>
      <div class="img" role="img" aria-label="Photo of rolls of packaging tape" style="left:12%;top:45%;width:50%;height:30%;background:radial-gradient(circle at 40% 40%,#e8edf5,#9fb3cf)"></div>
      <div class="foot"></div>
    </div>
    <div class="spine"></div>
    <div class="page inside" style="width:185px;height:262px">
      <div class="tab right">FEATURES &amp; BENEFITS</div>
      <div class="title" style="left:10%;top:22%">Stretch Film</div>
      <div class="body" style="left:10%;top:29%;width:80%">Cast and blown films in every gauge<br>Strong hold with clean unwind</div>
      <div class="title" style="left:10%;top:44%;font-size:7px">Colour options</div>
      <div class="swatches" style="left:10%;top:50%;width:80%">
        <span style="background:#1f4fa3"></span><span style="background:#d62b2b"></span><span style="background:#f2c230"></span><span style="background:#2f9e4a"></span><span style="background:#222"></span><span style="background:#e4e4e4"></span>
        <span style="background:#e97a1f"></span><span style="background:#7a3fa0"></span><span style="background:#4d8fd6"></span><span style="background:#8a5a2b"></span><span style="background:#d8e83a"></span><span style="background:#c7c7c7"></span>
      </div>
      <div class="img" role="img" aria-label="Photo of a stretch film roll" style="left:10%;top:66%;width:80%;height:22%;background:linear-gradient(90deg,#dfe6ef,#b6c5da)"></div>
      <div class="foot"></div>
    </div>
  </div>
  <p class="caption" style="top:280px">Inside Pages 2 &amp; 3</p>
</section>

<!-- Inside pages 4 & 5 -->
<section class="piece" style="left:429px;top:610px;width:390px;height:340px">
  <div class="spread" style="left:10px;top:0">
    <div class="page inside" style="width:185px;height:262px">
      <div class="tab left">MATERIALS</div>
      <div class="title" style="left:12%;top:22%">Packaging Tape</div>
      <div class="body" style="left:12%;top:29%;width:76%">Acrylic, hot melt and natural rubber<br>Printed tape on request</div>
      <div class="img" role="img" aria-label="Photo of coloured tape and film rolls" style="left:0;top:55%;width:85%;height:35%;background:linear-gradient(135deg,#1d1d22,#3b5fa8 55%,#e24aa0)"></div>
      <div class="foot"></div>
    </div>
    <div class="spine"></div>
    <div class="page inside" style="width:185px;height:262px">
      <div class="tab right">CAPABILITIES</div>
      <div class="title" style="left:10%;top:22%">Liners</div>
      <div class="body" style="left:10%;top:29%;width:80%">Custom liners for bags and boxes</div>
      <table class="spec" style="left:10%;top:38%;width:80%">
        <tr><th>Size</th><th>Length</th><th>Gauge</th></tr>
        <tr><td>48mm</td><td>100m</td><td>1.8mil</td></tr>
        <tr><td>72mm</td><td>100m</td><td>2.0mil</td></tr>
        <tr><td>96mm</td><td>50m</td><td>2.6mil</td></tr>
      </table>
      <div class="img" role="img" aria-label="Photo of a bulk bag liner" style="left:10%;top:64%;width:80%;height:24%;background:linear-gradient(180deg,#eef2f7,#c3cfdf)"></div>
      <div class="foot"></div>
    </div>
  </div>
  <p class="caption" style="top:280px">Inside Pages 4 &amp; 5</p>
</section>

</body>
</html>
```